Cookie Box Packaging

We are looking for a Box for our Shortbread Cookies. They are traditional shortbread middle to high end of the market. Made with butter. We already have a successful product and would like to use the brand but not necessarily the style.

We like our design to be an mix of vintage and modern - we are open to all colours. The competition on the supermarket shelf is stiff and we need to stand out in grocery not in the gourmet food market. Our thinking is simple rather than the craziness and chaos that comes with a supermarket shelf.
Attached are some Box Ideas, created in-house, along with a black shortbread box idea , which we loved but didn't really fit into the grocery section of the supermarket. Make us stand out in the grocery shelf! I have also uploaded a logo. Our brand is not necessary but, is there if you wanted to use it. I have also uploaded our other product/packet design so you can see the brand of our other cookie which is positioned in bakery /deli not grocery.

I look forward to seeing the results

```html
<!DOCTYPE html>
<html lang="en">
<head>
<meta charset="utf-8">
<title>Linden Bakehouse – Butter Shortbread Box Dieline</title>
<link rel="stylesheet" href="https://fonts.googleapis.com/css2?family=Archivo:wght@400;600;700&display=swap">
<style>
  :root {
    --page: #ffffff;
    --board: #fde3cf;
    --band-deep: #d9461c;
    --band-bright: #ff7a1a;
    --band-soft: #ffa34a;
    --brand-pink: #e78ac3;
    --ink: #1d1b1a;
    --seal-blue: #2a7fc6;
    --crumb-light: #f3dcc0;
    --crumb-dark: #d9b68d;
    --weight-ink: #ffe6d6;
  }
  * { margin: 0; padding: 0; box-sizing: border-box; }
  html, body {
    width: 1200px;
    height: 1007px;
    overflow: hidden;
    background: var(--page);
  }
  .canvas {
    position: relative;
    width: 1200px;
    height: 1007px;
    background: var(--page);
  }
  .dieline {
    position: absolute;
    left: 64px;
    top: 162px;
    width: 1072px;
    height: 683px;
  }
  .panel { fill: var(--board); }
  .band-deep { fill: var(--band-deep); }
  .band-bright { fill: var(--band-bright); }
  .band-soft { fill: var(--band-soft); }
  .copy {
    font-family: "Archivo", Arial, sans-serif;
    font-weight: 600;
    font-size: 14.5px;
    fill: var(--ink);
    letter-spacing: 0.3px;
  }
  .brand-name {
    font-family: "Archivo", Arial, sans-serif;
    font-weight: 700;
    font-size: 40px;
    fill: var(--brand-pink);
  }
  .product-name {
    font-family: "Archivo", Arial, sans-serif;
    font-weight: 700;
    font-size: 24px;
    fill: var(--ink);
    letter-spacing: 0.6px;
  }
  .product-flavour {
    font-family: "Archivo", Arial, sans-serif;
    font-weight: 600;
    font-size: 13px;
    fill: var(--ink);
    letter-spacing: 0.5px;
  }
  .net-weight {
    font-family: "Archivo", Arial, sans-serif;
    font-weight: 600;
    font-size: 15px;
    fill: var(--weight-ink);
  }
  .origin-seal { fill: var(--seal-blue); }
</style>
</head>
<body>
<main class="canvas">
  <svg class="dieline" viewBox="0 0 1072 683" xmlns="http://www.w3.org/2000/svg">
    <defs>
      <linearGradient id="crumbGlow" x1="0" y1="0" x2="1" y2="1">
        <stop offset="0" stop-color="var(--crumb-light)" stop-opacity="0"/>
        <stop offset="0.5" stop-color="var(--crumb-light)" stop-opacity="0.8"/>
        <stop offset="1" stop-color="var(--crumb-light)" stop-opacity="0.2"/>
      </linearGradient>
      <linearGradient id="cookieStack" x1="0" y1="0" x2="0" y2="1">
        <stop offset="0" stop-color="#f0d6b0"/>
        <stop offset="1" stop-color="var(--crumb-dark)"/>
      </linearGradient>
      <clipPath id="frontClip"><rect x="223" y="0" width="621" height="683"/></clipPath>
    </defs>

    <!-- side flaps -->
    <rect class="panel side-flap side-flap--left" x="0" y="228" width="223" height="225"/>
    <rect class="panel side-flap side-flap--right" x="844" y="228" width="228" height="225"/>

    <!-- main column: lid flap, front face, base -->
    <rect class="panel front-column" x="223" y="0" width="621" height="683"/>

    <g clip-path="url(#frontClip)">
      <rect role="img" aria-label="Faint close-up photo of crumbly butter shortbread" x="260" y="290" width="420" height="200" rx="60" fill="url(#crumbGlow)"/>

      <!-- upper swoosh -->
      <path class="band-deep" d="M223,212 C420,168 640,168 844,184 L844,232 C640,214 430,232 223,278 Z"/>
      <path class="band-bright" d="M223,262 C430,222 640,212 844,222 L844,244 C640,236 430,250 223,296 Z"/>

      <!-- lower swoosh -->
      <path class="band-deep" d="M223,498 C430,472 640,444 844,428 L844,468 C640,484 430,512 223,536 Z"/>
      <path class="band-bright" d="M223,528 C430,506 640,478 844,460 L844,500 C640,516 430,540 223,556 Z"/>
      <path class="band-soft" d="M223,552 C430,536 640,512 844,496 L844,506 C640,524 430,548 223,562 Z"/>
    </g>

    <!-- lid flap copy -->
    <g class="lid-copy" transform="rotate(180 534 92)">
      <text class="copy" x="246" y="58">Creamed. kneaded. extruded. cut &amp; baked to perfection</text>
      <text class="copy" x="246" y="82">Ingredients: Butter, Flour, Sugar, Cornstarch, Cream</text>
      <text class="copy" x="246" y="106">they way your grannie used to make them.</text>
      <text class="copy" x="246" y="130">You can taste the history in every decadent mouthful</text>
    </g>

    <!-- brand -->
    <g class="brand">
      <circle cx="268" cy="376" r="10" fill="var(--brand-pink)"/>
      <text class="brand-name" x="288" y="390">Linden</text>
      <text class="brand-name" x="288" y="428" style="font-size:26px">Bakehouse</text>
    </g>

    <!-- product -->
    <rect role="img" aria-label="Photo of a stack of round butter shortbread cookies" x="676" y="253" width="97" height="108" rx="30" fill="url(#cookieStack)"/>
    <text class="product-name" x="580" y="398">SHORTBREAD</text>
    <text class="product-flavour" x="722" y="428">BUTTER</text>
    <text class="net-weight" x="500" y="490">250 g</text>

    <!-- origin seal on left flap -->
    <circle class="origin-seal" cx="136" cy="300" r="50"/>

    <!-- base copy -->
    <g class="base-copy">
      <text class="copy" x="246" y="596">Creamed. kneaded. extruded. cut &amp; baked to perfection</text>
      <text class="copy" x="246" y="620">Ingredients: Butter, Flour, Sugar, Cornstarch, Cream</text>
      <text class="copy" x="246" y="644">they way your grannie used to make them.</text>
      <text class="copy" x="246" y="668">You can taste the history in every decadent mouthful</text>
    </g>
  </svg>
</main>
</body>
</html>
```